Branding Quarter WeB Page

The Branding Quarter is a marketing innovation agency that works with business to drive growth through innovation. It is run by myself and I would like the website to contain the a mechanism to capture email addresses for a database, a blog, a tab about myself and what I do. I have a design device that I have started to use, but I am looking for more of a hand written font to be used - reflecting creativity and clarity. My current blog is at www.brandingquarter.me
Updates

This project should be wordpress design, not webpage design...

Many thanks, Lou

Target Market(s)

Brand Marketers who are looking for support

Industry/Entity Type

Marketing

Requirements
Must have
• Blog
Tabs
Email Collection
Twitter feed
Links to Linkedin, Twitter, google+
Enable self editing
Needs to look very stylised and innovative!

```html
<!DOCTYPE html>
<html lang="en">
<head>
<meta charset="utf-8">
<title>The Branding Quarter</title>
<link href="https://fonts.googleapis.com/css2?family=Gochi+Hand&family=Quicksand:wght@300;400;500;700&family=Arimo:wght@400;700&display=swap" rel="stylesheet">
<style>
  :root {
    --page-bg: #1f1f1f;
    --page-bg-light: #262626;
    --accent: #f4d60f;
    --card-bg: #ffffff;
    --title-ink: #3b3b3b;
    --body-ink: #7a7a7a;
    --nav-ink: #d9d9d9;
    --footer-head: #8a8a8a;
    --footer-ink: #6e6e6e;
    --button-dark: #3a3a3a;
    --hero-dark: #2c2c2c;
    --hero-mid: #4a4a4a;
  }
  * { box-sizing: border-box; margin: 0; padding: 0; }
  html, body { width: 1200px; height: 3449px; overflow: hidden; }
  body {
    position: relative;
    background: repeating-linear-gradient(45deg, var(--page-bg) 0 3px, var(--page-bg-light) 3px 5px);
    font-family: "Quicksand", sans-serif;
  }

  /* Header */
  .site-header { position: absolute; left: 0; top: 0; width: 1200px; height: 125px; }
  .brand { position: absolute; left: 72px; top: 42px; }
  .brand-name { font-family: "Quicksand", sans-serif; font-weight: 700; font-size: 28px; line-height: 30px; color: #ffffff; }
  .brand-tagline { font-family: "Quicksand", sans-serif; font-weight: 500; font-size: 14px; line-height: 20px; color: var(--nav-ink); }
  .main-nav { position: absolute; right: 70px; top: 61px; display: flex; align-items: center; gap: 22px; }
  .main-nav a { font-family: "Arimo", sans-serif; font-size: 13px; color: var(--nav-ink); text-decoration: none; letter-spacing: 0.3px; }
  .main-nav svg { display: block; }

  /* Posts */
  .post-card { position: absolute; left: 70px; width: 1058px; height: 715px; background: var(--card-bg); }
  .post-hero {
    position: relative; height: 458px;
    background: linear-gradient(100deg, var(--hero-mid) 0%, var(--hero-dark) 35%, #3a3a3a 70%, #333 100%);
    border-left: 3px solid var(--accent);
  }
  .post-hero-words {
    position: absolute; left: 0; right: 0; top: 160px; padding-left: 340px; text-align: center;
    font-family: "Gochi Hand", cursive; color: var(--accent); font-size: 66px; line-height: 66px;
  }
  .post-title {
    margin-top: 18px; text-align: center; font-weight: 300; font-size: 43px; color: var(--title-ink);
  }
  .post-excerpt {
    width: 810px; margin: 14px auto 0; text-align: center; font-size: 14.5px; line-height: 25px; color: var(--body-ink); font-weight: 400;
  }
  .read-more {
    display: flex; width: 144px; height: 26px; margin: 18px auto 0; border: 1px solid var(--accent);
    align-items: center; text-decoration: none;
  }
  .read-more-icon { width: 26px; height: 26px; background: var(--accent); display: flex; align-items: center; justify-content: center; }
  .read-more-label { flex: 1; text-align: center; font-family: "Arimo", sans-serif; font-size: 11px; font-weight: 700; color: var(--title-ink); letter-spacing: 0.4px; }

  /* Pagination */
  .next-page {
    position: absolute; left: 542px; top: 3138px; width: 116px; height: 30px; background: var(--button-dark);
    color: #e6e6e6; font-family: "Arimo", sans-serif; font-size: 12px; text-align: center; line-height: 30px; text-decoration: none;
  }

  /* Footer widgets */
  .footer-widgets { position: absolute; left: 70px; top: 3218px; width: 1058px; display: flex; justify-content: space-between; }
  .widget { width: 240px; text-align: center; }
  .widget-title {
    font-weight: 300; font-size: 20px; color: var(--footer-head); padding-bottom: 6px; white-space: nowrap;
    border-bottom: 1px solid #3c3c3c; margin: 0 16px 12px;
  }
  .widget p, .widget li { font-size: 12px; line-height: 20px; color: var(--footer-ink); list-style: none; }
  .widget .link { color: var(--accent); }
  .widget .name { color: var(--footer-ink); }

  /* Bottom bar */
  .site-footer {
    position: absolute; left: 0; top: 3401px; width: 1200px; height: 48px; background: var(--accent);
    display: flex; align-items: center; justify-content: space-between; padding: 0 72px;
  }
  .copyright { font-family: "Arimo", sans-serif; font-size: 12px; color: #2a2a2a; }
  .footer-brand-name { font-family: "Quicksand", sans-serif; font-weight: 700; font-size: 18px; color: #1f1f1f; }
</style>
</head>
<body>

<header class="site-header">
  <div class="brand">
    <div class="brand-name">The Branding Quarter</div>
    <div class="brand-tagline">News and Ideas for Brand Marketers</div>
  </div>
  <nav class="main-nav">
    <a href="#">HOME</a>
    <a href="#">LOU HARWELL</a>
    <a href="#">ABOUT "THE BRANDING QUARTER"</a>
    <a href="#">TWITTER FEED</a>
    <a href="#">CONTACT</a>
    <svg width="16" height="16" viewBox="0 0 16 16" aria-label="Search"><circle cx="6.5" cy="6.5" r="4.5" fill="none" stroke="#f4d60f" stroke-width="2.2"/><line x1="10" y1="10" x2="14.5" y2="14.5" stroke="#f4d60f" stroke-width="2.6" stroke-linecap="round"/></svg>
  </nav>
</header>

<main>
  <article class="post-card" style="top:125px">
    <div class="post-hero" role="img" aria-label="Photo of a thoughtful man in a suit on a dark grey backdrop">
      <div class="post-hero-words">Welcome to<br>The Branding Quarter</div>
    </div>
    <h2 class="post-title">Welcome to The Branding Quarter</h2>
    <p class="post-excerpt">Our aim is really simple – we wanted to create a space for you, the brand manager, marketing professional, to connect easily and enjoyably to the latest developments in our industry. Whether it be research, insights, branding, sponsorship, pr, advertising, design or good pure and simple marketing strategy we are here to help provide you with the latest in an increasingly fragmented and evolving industry.</p>
    <a class="read-more" href="#"><span class="read-more-icon"><svg width="12" height="12" viewBox="0 0 12 12"><path d="M1 6 L6 1 L11 1 L11 6 L6 11 Z" fill="none" stroke="#1f1f1f" stroke-width="1.6"/><circle cx="8.5" cy="3.5" r="1" fill="#1f1f1f"/></svg></span><span class="read-more-label">READ MORE</span></a>
  </article>

  <article class="post-card" style="top:875px">
    <div class="post-hero" role="img" aria-label="Photo of a thoughtful man in a suit on a dark grey backdrop">
      <div class="post-hero-words">Welcome to<br>The Branding Quarter</div>
    </div>
    <h2 class="post-title">Welcome to The Branding Quarter</h2>
    <p class="post-excerpt">Our aim is really simple – we wanted to create a space for you, the brand manager, marketing professional, to connect easily and enjoyably to the latest developments in our industry. Whether it be research, insights, branding, sponsorship, pr, advertising, design or good pure and simple marketing strategy we are here to help provide you with the latest in an increasingly fragmented and evolving industry.</p>
    <a class="read-more" href="#"><span class="read-more-icon"><svg width="12" height="12" viewBox="0 0 12 12"><path d="M1 6 L6 1 L11 1 L11 6 L6 11 Z" fill="none" stroke="#1f1f1f" stroke-width="1.6"/><circle cx="8.5" cy="3.5" r="1" fill="#1f1f1f"/></svg></span><span class="read-more-label">READ MORE</span></a>
  </article>

  <article class="post-card" style="top:1628px">
    <div class="post-hero" role="img" aria-label="Photo of a thoughtful man in a suit on a dark grey backdrop">
      <div class="post-hero-words">Welcome to<br>The Branding Quarter</div>
    </div>
    <h2 class="post-title">Welcome to The Branding Quarter</h2>
    <p class="post-excerpt">Our aim is really simple – we wanted to create a space for you, the brand manager, marketing professional, to connect easily and enjoyably to the latest developments in our industry. Whether it be research, insights, branding, sponsorship, pr, advertising, design or good pure and simple marketing strategy we are here to help provide you with the latest in an increasingly fragmented and evolving industry.</p>
    <a class="read-more" href="#"><span class="read-more-icon"><svg width="12" height="12" viewBox="0 0 12 12"><path d="M1 6 L6 1 L11 1 L11 6 L6 11 Z" fill="none" stroke="#1f1f1f" stroke-width="1.6"/><circle cx="8.5" cy="3.5" r="1" fill="#1f1f1f"/></svg></span><span class="read-more-label">READ MORE</span></a>
  </article>

  <article class="post-card" style="top:2381px">
    <div class="post-hero" role="img" aria-label="Photo of a thoughtful man in a suit on a dark grey backdrop">
      <div class="post-hero-words">Welcome to<br>The Branding Quarter</div>
    </div>
    <h2 class="post-title">Welcome to The Branding Quarter</h2>
    <p class="post-excerpt">Our aim is really simple – we wanted to create a space for you, the brand manager, marketing professional, to connect easily and enjoyably to the latest developments in our industry. Whether it be research, insights, branding, sponsorship, pr, advertising, design or good pure and simple marketing strategy we are here to help provide you with the latest in an increasingly fragmented and evolving industry.</p>
    <a class="read-more" href="#"><span class="read-more-icon"><svg width="12" height="12" viewBox="0 0 12 12"><path d="M1 6 L6 1 L11 1 L11 6 L6 11 Z" fill="none" stroke="#1f1f1f" stroke-width="1.6"/><circle cx="8.5" cy="3.5" r="1" fill="#1f1f1f"/></svg></span><span class="read-more-label">READ MORE</span></a>
  </article>

  <a class="next-page" href="#">NEXT PAGE »</a>
</main>

<section class="footer-widgets">
  <div class="widget">
    <h3 class="widget-title">Recent Posts</h3>
    <ul>
      <li class="link">This Is A Standard Post With Featured Image</li>
      <li class="link">twitter.com/the branding quarter</li>
      <li class="link">the branding quarter the branding quarter</li>
    </ul>
  </div>
  <div class="widget">
    <h3 class="widget-title">Who is "Lou Harwell"</h3>
    <p>some text goes here, some text goes here, some text goes here, some text goes here, some text goes here, some text goes here,</p>
  </div>
  <div class="widget">
    <h3 class="widget-title">Recent Comments</h3>
    <ul>
      <li><span class="name">Marco</span> on <span class="link">Recent post comment goes here :) (:)</span></li>
      <li><span class="name">Ned Ray</span> on <span class="link">The True European City Of Love Gallery</span></li>
      <li><span class="name">admin</span> on <span class="link">The True European City Of Love</span></li>
    </ul>
  </div>
  <div class="widget">
    <h3 class="widget-title">Latest Tweet</h3>
  </div>
</section>

<footer class="site-footer">
  <span class="copyright">Copyright © 2013</span>
  <span class="footer-brand-name">The Branding Quarter</span>
</footer>

</body>
</html>
```